Flyer for Compassion training days

I need a A5-size, single-sided flyer design for my training days. They are weekends in a blend of Compassionate Communication and Buddhist teachings called Palomere Communication. The logo for Palomere that should be included.
The flyer needs room for 1) course title, 2) course dates, location & price, 3) course description, 4) booking info, 5) my picture & short bio, and 6) the palomere.co website (yes, it is 'co' and not 'com).
Updates

Target Market(s)

Women 35-65 years, well-educated, spiritually minded. May have interests like yoga and meditation.

Industry/Entity Type

Health And Wellness

Font styles to use
Sans Serif
Other font styles liked:
• Blue Plaque, Josefina are both great

Colors
fbf289
fdf9cf
cfeae6
33b8a4

Requirements
Must have
• The Palomere logo; my picture.
• Elegance. Calm and expansive feel.
• The poster provided in the project files shows you the kind of information I need to include.
• Colours -- greens and yellows, but the options on pixel harbor are not quite the right shades.
• The logo colour can be changed.
Nice to have
• Classy (but not cliche) image associated with Buddhism; gentle curves similar to those on the business card (see project files).
Should not have
• Dark background. Busy, loud design. Overly 'swirly' design. Images that I have to buy separately.

```html
<!DOCTYPE html>
<html lang="en">
<head>
<meta charset="utf-8">
<title>Palomere Communication – Core Course Flyer</title>
<link rel="stylesheet" href="https://fonts.googleapis.com/css2?family=Lato:wght@400;700&family=Playfair+Display:wght@700;800&display=swap">
<style>
  :root {
    --page-bg: #d9d9d6;
    --paper: #ffffff;
    --cream-band: #ead7c6;
    --cream-band-light: #f2e5d9;
    --title-brown: #7b5a48;
    --tagline-tan: #a9896c;
    --date-red: #b4574a;
    --location-brown: #6d5a4f;
    --leaf-green: #6bbd3c;
    --logo-green: #3fae4a;
    --meadow-light: #9fd07c;
    --meadow-mid: #6fb24f;
    --meadow-dark: #4f8f3a;
    --lotus-pink: #ec6fa6;
    --lotus-light: #f7c6dc;
    --portrait-tone: #a88f6e;
    --portrait-frame: #e0c9ae;
    --web-red: #a5514a;
    --white: #ffffff;
  }
  * { box-sizing: border-box; margin: 0; padding: 0; }
  html, body { width: 969px; height: 1200px; overflow: hidden; }
  body { background: var(--page-bg); position: relative; font-family: "Lato", sans-serif; }

  .flyer {
    position: absolute; left: 75px; top: 20px;
    width: 775px; height: 1099px;
    background: var(--paper);
    transform: scale(1.055); transform-origin: top left;
    overflow: hidden;
  }

  .lotus-photo {
    position: absolute; right: 0; top: 0; width: 230px; height: 330px;
    background: radial-gradient(ellipse at 85% 25%, var(--lotus-pink) 0%, var(--lotus-light) 55%, rgba(255,255,255,0) 78%);
  }

  .brand-mark { position: absolute; left: 26px; top: 70px; display: flex; align-items: center; gap: 10px; }
  .brand-mark .dot { width: 34px; height: 34px; border-radius: 50%; background: var(--logo-green); }
  .brand-mark .name { font-family: "Lato", sans-serif; font-weight: 700; font-size: 30px; color: var(--logo-green); }

  .tagline {
    position: absolute; left: 150px; width: 480px; top: 130px; text-align: center;
    font-family: "Playfair Display", serif; font-weight: 700; font-size: 22px; line-height: 27px;
    color: var(--tagline-tan);
  }
  .course-title {
    position: absolute; left: 60px; width: 640px; top: 190px; text-align: center;
    font-family: "Playfair Display", serif; font-weight: 800; color: var(--title-brown);
    line-height: 0.92;
  }
  .course-title .line-one { display: block; font-size: 64px; }
  .course-title .line-two { display: block; font-size: 70px; }
  .course-kind {
    position: absolute; left: 0; width: 775px; top: 330px; text-align: center;
    font-size: 31px; color: var(--leaf-green); letter-spacing: 0.5px;
  }

  .band-svg { position: absolute; left: 0; top: 0; width: 775px; height: 1099px; }

  .meadow-photo { position: absolute; inset: 0; }

  .event-details { position: absolute; left: 0; width: 775px; top: 386px; text-align: center; }
  .event-date { font-family: "Playfair Display", serif; font-weight: 800; font-size: 38px; color: var(--date-red); line-height: 44px; }
  .event-date small { font-size: 28px; }
  .event-venue { font-size: 23px; color: var(--location-brown); line-height: 28px; }
  .event-price { font-size: 14px; color: var(--location-brown); line-height: 22px; }

  .body-copy { position: absolute; color: var(--white); font-size: 16px; line-height: 18.5px; }
  .course-description { left: 63px; top: 514px; width: 325px; }
  .course-description p { margin-bottom: 18px; }
  .topic-list { list-style: none; }
  .topic-list li { position: relative; padding-left: 23px; margin-bottom: 18px; }
  .topic-list li::before {
    content: ""; position: absolute; left: 2px; top: 6px; width: 8px; height: 8px;
    border-radius: 50%; background: var(--white);
  }
  .topic-list + p { margin-top: -4px; }

  .booking-info { left: 405px; top: 514px; width: 320px; }
  .facilitator-bio { left: 405px; top: 877px; width: 320px; }
  .facilitator-bio p { margin-bottom: 18px; }

  .portrait {
    position: absolute; left: 403px; top: 565px; width: 296px; height: 296px; border-radius: 50%;
    border: 3px solid var(--portrait-frame);
    background: radial-gradient(circle at 50% 45%, #c8b291 0%, var(--portrait-tone) 55%, #6e5a44 100%);
  }

  .website {
    position: absolute; left: 0; width: 775px; top: 1058px; text-align: center;
    font-size: 18px; font-weight: 700; color: var(--web-red);
  }
</style>
</head>
<body>
  <main class="flyer">
    <svg class="band-svg" viewBox="0 0 775 1099" aria-hidden="true">
      <defs>
        <linearGradient id="meadowFill" x1="0" y1="0" x2="0" y2="1">
          <stop offset="0" stop-color="#7cbf55"/>
          <stop offset="0.5" stop-color="#8cc866"/>
          <stop offset="1" stop-color="#5f9e43"/>
        </linearGradient>
        <linearGradient id="bandFill" x1="0" y1="0" x2="0" y2="1">
          <stop offset="0" stop-color="#ecdacb"/>
          <stop offset="1" stop-color="#e5cfbd"/>
        </linearGradient>
      </defs>
      <path d="M0 480 C 200 470, 500 505, 775 478 L775 1050 C 520 1020, 260 1060, 0 1030 Z" fill="url(#meadowFill)" role="img" aria-label="Soft meadow photograph with a calm seated Buddha statue"/>
      <path d="M0 360 C 220 345, 520 380, 775 350 L775 478 C 500 505, 200 470, 0 485 Z" fill="url(#bandFill)"/>
      <path d="M0 1030 C 260 1060, 520 1020, 775 1045 L775 1099 L0 1099 Z" fill="var(--cream-band)"/>
    </svg>

    <div class="lotus-photo" role="img" aria-label="Close-up of a pink lotus flower"></div>

    <div class="brand-mark">
      <span class="dot"></span>
      <span class="name">Palomere</span>
    </div>

    <p class="tagline">Mindfulness + Kindness +<br>Compassionate Communication =</p>
    <h1 class="course-title"><span class="line-one">Palomere</span><span class="line-two">Communication</span></h1>
    <p class="course-kind">CORE COURSE</p>

    <section class="event-details">
      <p class="event-date">11–12<small>Dec</small></p>
      <p class="event-venue">Linden House Centre, Edinburgh</p>
      <p class="event-price">(£125/100)</p>
    </section>

    <section class="body-copy course-description">
      <p>Palomere Communication can help you increase awareness &amp; compassion in everyday speech (with yourself &amp; others), better understand your own patterns, and build resilience to challenging situations. Choose from:</p>
      <p>In this 2-day Core Course, we’ll explore:</p>
      <ul class="topic-list">
        <li>Compassionate Communication;</li>
        <li>Buddhist teachings on Right Speech, loving-kindness, Right Effort, and more;</li>
        <li>mindfulness practices;</li>
        <li>choices available to us in our everyday speech.</li>
      </ul>
      <p>This workshop will be of interest if you’d like to improve personal and/or professional relationships.  Open to all, best suited to those with at least 1 year’s experience with Mindfulness, Buddhism, or Compassionate Communication / NVC.</p>
    </section>

    <section class="body-copy booking-info">
      <p>Booking: Book online at TicketLeaf or write maren@palomere.co</p>
    </section>

    <div class="portrait" role="img" aria-label="Portrait photograph of the facilitator, Maren Holloway"></div>

    <section class="body-copy facilitator-bio">
      <p>Facilitator:  Maren Holloway is an experienced group facilitator, having worked with a range of organisations and presented at a number of festivals &amp; conferences.</p>
      <p>Maren offers coaching in Palomere Communication.</p>
    </section>

    <p class="website">www.palomere.co</p>
  </main>
</body>
</html>
```